Business card design needed

We are a start up Mobile Vet Clinic.
We will be servicing an are that cover the Gladstone Region Shire.
Bookings will be made via the number listed or email address.
Travel will be charged

Target Market(s)

Pet Owners

Industry/Entity Type

Business

Contact Information for Business Card

BRINDELLA MOBILE VET
Tarrowen Pty Ltd
Dana Fosterby BVSc
27 Wexhaven St
Calliope QLD 4680

PH: 0743186209 Fax: 0743186514 email: bmvet@quillnet.example

Logo styles of interest
Pictorial/Combination Logo

```html
<!DOCTYPE html>
<html lang="en">
<head>
<meta charset="utf-8">
<title>Brindella Mobile Vet – Business Card</title>
<link rel="stylesheet" href="https://fonts.googleapis.com/css2?family=Tinos&display=swap">
<style>
  :root {
    --teal: #5bbea8;
    --teal-light: #79cbb8;
    --edge-shadow: #1f3d35;
    --paper: #f5f5f5;
    --strip: #e5f3ee;
    --ink: #111111;
    --white: #ffffff;
  }
  * { margin: 0; padding: 0; box-sizing: border-box; }
  html, body {
    width: 1200px;
    height: 693px;
    overflow: hidden;
    background: var(--paper);
  }
  .card {
    position: relative;
    width: 1200px;
    height: 693px;
    background: var(--teal);
    overflow: hidden;
    font-family: "Tinos", "Times New Roman", serif;
  }
  .card__wave {
    position: absolute;
    inset: 0;
    width: 1200px;
    height: 693px;
  }
  .brand {
    position: absolute;
    left: 380px;
    top: 0;
    width: 460px;
    height: 600px;
    color: var(--white);
    text-align: center;
    font-weight: 400;
  }
  .brand__line {
    position: absolute;
    left: 0;
    width: 100%;
    line-height: 1;
    white-space: nowrap;
  }
  .brand__line--first { top: 102px; font-size: 88px; }
  .brand__line--second { top: 392px; font-size: 70px; }
  .brand__line--third { top: 478px; font-size: 60px; }
  .brand__dot {
    position: absolute;
    left: 160px;
    top: 222px;
    width: 140px;
    height: 140px;
    border-radius: 50%;
    background: var(--teal-light);
  }
  .contact-strip {
    position: absolute;
    left: 130px;
    top: 610px;
    width: 1070px;
    height: 39px;
    background: var(--strip);
    display: flex;
    align-items: center;
    padding-left: 28px;
    gap: 24px;
    color: var(--ink);
    font-size: 27px;
    white-space: nowrap;
  }
</style>
</head>
<body>
  <div class="card">
    <svg class="card__wave" viewBox="0 0 1200 693" aria-hidden="true">
      <path d="M0 0 H172 C200 60 196 130 180 230 C160 340 128 420 132 520 C136 600 160 660 184 693 H0 Z"
            fill="var(--edge-shadow)" opacity="0.85"/>
      <path d="M0 0 H164 C190 60 186 130 170 230 C150 340 118 420 122 520 C126 600 150 660 174 693 H0 Z"
            fill="var(--paper)"/>
    </svg>

    <div class="brand" aria-label="Brindella Mobile Vet">
      <div class="brand__line brand__line--first">Brindella</div>
      <div class="brand__dot"></div>
      <div class="brand__line brand__line--second">Mobile</div>
      <div class="brand__line brand__line--third">Vet</div>
    </div>

    <div class="contact-strip">
      <span class="contact-strip__item">Phone: 0743186209</span>
      <span class="contact-strip__item">Fax: 0743186514</span>
      <span class="contact-strip__item">email: bmvet@quillnet.example</span>
    </div>
  </div>
</body>
</html>
```